Loyalty Card

We are a chiropractic and massage practice in Williamsburg, Virginia. We would like to offer our patients a loyalty card for if they buy 7 (60 min) massages then they will get one free. (ex: like a 'punch card'), our staff members would make a special hole punch on the card every time they get an hour massage. We would have to have exclusions listed on the card though as well. (for example: cannot be combined with any other discount or offer. Cannot be combined with insurance, Medicare, auto accident or workmen's compensation claims)

Target Market(s)

Patients of chiropractic office who are currently receiving massage or interested in massage.

Industry/Entity Type

Massage

Colors
eb2027
474747
000000

Requirements
Nice to have
• I included a picture of a screenshot of our current gift card design which I like. It is the front and back of the gift card. It doesn't have any cheesy pictures on it, and looks very professional.
Should not have
• Do not want it to look like a SPA card. It is a professional chiropractic office, although do not want pictures of spines, etc.

```html
<!DOCTYPE html>
<html lang="en">
<head>
<meta charset="utf-8">
<title>Loyalty Card – Ashbury Posture Center</title>
<link rel="stylesheet" href="https://fonts.googleapis.com/css2?family=Cinzel:wght@400;600&family=Crimson+Text:wght@400&family=Open+Sans:wght@700;800&display=swap">
<style>
  :root {
    --brand-red: #c41e35;
    --brand-red-deep: #9e1429;
    --brand-red-soft: #d9475a;
    --charcoal: #474747;
    --ink: #000000;
    --paper: #ffffff;
    --stage: #e9e9e9;
    --mark-grey: #cfcfcf;
  }
  * { box-sizing: border-box; margin: 0; padding: 0; }
  html, body {
    width: 759px;
    height: 1200px;
    overflow: hidden;
    background: var(--stage);
  }
  .canvas {
    position: relative;
    width: 759px;
    height: 1200px;
  }

  /* ---------- shared card ---------- */
  .card {
    position: absolute;
    background: var(--paper);
    border-radius: 18px;
    overflow: hidden;
    box-shadow: 0 6px 18px rgba(0,0,0,0.18);
  }
  .title-loyalty {
    font-family: "Cinzel", serif;
    font-weight: 600;
    color: var(--paper);
    letter-spacing: 0.06em;
    text-align: center;
    white-space: nowrap;
  }
  .rule {
    display: block;
    height: 1px;
    background: rgba(255,255,255,0.75);
    margin: 0 auto;
  }
  .brand {
    display: flex;
    align-items: center;
    gap: 14px;
  }
  .brand-mark {
    flex: none;
    background: var(--mark-grey);
  }
  .brand-name {
    font-family: "Cinzel", serif;
    font-weight: 600;
    color: var(--brand-red);
    letter-spacing: 0.08em;
    line-height: 1.15;
    text-transform: uppercase;
  }

  /* ---------- front ---------- */
  .card-front {
    left: 60px;
    top: 60px;
    width: 640px;
    height: 366px;
    display: flex;
  }
  .front-band {
    width: 282px;
    height: 100%;
    background: linear-gradient(180deg, var(--brand-red) 0%, var(--brand-red-deep) 100%);
    display: flex;
    flex-direction: column;
    justify-content: center;
    gap: 18px;
  }
  .front-band .rule { width: 150px; }
  .front-band .title-loyalty { font-size: 34px; }
  .front-body {
    flex: 1;
    display: flex;
    align-items: center;
    justify-content: center;
  }
  .front-body .brand-mark { width: 62px; height: 62px; }
  .front-body .brand-name { font-size: 28px; }

  /* ---------- back ---------- */
  .card-back {
    left: 196px;
    top: 486px;
    width: 366px;
    height: 640px;
  }
  .back-top {
    height: 82px;
    background: linear-gradient(180deg, var(--brand-red) 0%, var(--brand-red-deep) 100%);
    display: flex;
    align-items: center;
    justify-content: center;
  }
  .back-top .title-loyalty { font-size: 30px; }
  .back-body {
    padding: 26px 28px 0;
  }
  .back-body .brand { justify-content: center; }
  .back-body .brand-mark { width: 40px; height: 40px; }
  .back-body .brand-name { font-size: 21px; }
  .offer {
    margin-top: 18px;
    font-family: "Crimson Text", serif;
    font-size: 19px;
    line-height: 1.2;
    color: var(--charcoal);
    text-align: center;
  }
  .punch-grid {
    position: relative;
    margin: 26px auto 0;
    width: 270px;
    height: 250px;
  }
  .punch {
    position: absolute;
    width: 60px;
    height: 60px;
    border-radius: 50%;
    background: var(--brand-red);
    box-shadow: inset 0 0 0 4px var(--brand-red-deep), inset 0 0 0 6px var(--brand-red-soft);
    font-family: "Crimson Text", serif;
    font-size: 28px;
    line-height: 60px;
    text-align: center;
    color: var(--paper);
  }
  .punch-free {
    background: var(--charcoal);
    box-shadow: inset 0 0 0 4px #2e2e2e, inset 0 0 0 6px #6a6a6a;
  }
  .punch.p1 { left: 0;     top: 0; }
  .punch.p2 { left: 105px; top: 0; }
  .punch.p3 { left: 210px; top: 0; }
  .punch.p4 { left: 0;     top: 90px; }
  .punch.p5 { left: 105px; top: 90px; }
  .punch.p6 { left: 210px; top: 90px; }
  .punch.p7 { left: 0;     top: 180px; }
  .punch.p8 { left: 105px; top: 180px; }
  .free-pointer {
    position: absolute;
    left: 172px;
    top: 176px;
    width: 60px;
    height: 34px;
  }
  .free-label {
    position: absolute;
    left: 196px;
    top: 214px;
    font-family: "Open Sans", sans-serif;
    font-weight: 800;
    font-size: 15px;
    color: var(--ink);
  }
  .back-bottom {
    position: absolute;
    left: 0;
    bottom: 0;
    width: 100%;
    height: 92px;
    background: linear-gradient(180deg, var(--brand-red) 0%, var(--brand-red-deep) 100%);
    display: flex;
    align-items: center;
    justify-content: center;
    padding: 0 18px;
  }
  .exclusions {
    font-family: "Open Sans", sans-serif;
    font-weight: 700;
    font-size: 11.5px;
    line-height: 1.45;
    color: var(--paper);
    text-align: center;
  }
</style>
</head>
<body>
<main class="canvas">

  <section class="card card-front" aria-label="Loyalty card, front">
    <div class="front-band">
      <span class="rule"></span>
      <h1 class="title-loyalty">Loyalty Card</h1>
      <span class="rule"></span>
    </div>
    <div class="front-body">
      <div class="brand">
        <span class="brand-mark"></span>
        <p class="brand-name">Ashbury<br>Posture Center</p>
      </div>
    </div>
  </section>

  <section class="card card-back" aria-label="Loyalty card, back">
    <header class="back-top">
      <h2 class="title-loyalty">Loyalty Card</h2>
    </header>
    <div class="back-body">
      <div class="brand">
        <span class="brand-mark"></span>
        <p class="brand-name">Ashbury<br>Posture Center</p>
      </div>
      <p class="offer">If you buy 7 (60 min) massages,<br>then you will get one free</p>
      <div class="punch-grid">
        <span class="punch p1">1</span>
        <span class="punch p2">2</span>
        <span class="punch p3">3</span>
        <span class="punch p4">4</span>
        <span class="punch p5">5</span>
        <span class="punch p6">6</span>
        <span class="punch p7">7</span>
        <span class="punch p8 punch-free">8</span>
        <svg class="free-pointer" viewBox="0 0 60 34" aria-hidden="true">
          <path d="M52 30 C46 10 28 4 8 10" fill="none" stroke="#000" stroke-width="2"/>
          <path d="M14 4 L6 10 L15 15" fill="none" stroke="#000" stroke-width="2" stroke-linejoin="round"/>
        </svg>
        <span class="free-label">FREE !</span>
      </div>
    </div>
    <footer class="back-bottom">
      <p class="exclusions">Cannot be combined with any other discount or offer.<br>Cannot be combined with Insurance, Medicare,<br>Auto Accident or Workmen's Compensation Claims</p>
    </footer>
  </section>

</main>
</body>
</html>
```